Fenwick Nutrition Therapy needs a business card design

I need a business card design for my private practice. Green is my favorite color. I would like the back of the card to include an area for future appointment dates and time. I provide nutrition therapy to individuals, groups and families. I work a lot with adolescents and women who have eating disorders, but also work with athletes.
Updates

Reason: I received several new designs and would like to take some time reviewing them.

Target Market(s)

I am working primarily with women, but also men (mostly athletes). I work with a lot of runners. I work with people who are 14-60's.

Industry/Entity Type

Nutrition

Font styles to use
Serif
Sans Serif

Colors
9bcb3c
acd037

Requirements
Nice to have
• I would love to have 'Fenwick' incorporated into the design since it is my last name. If possible, I'd love to have an actual moon if it looks professional.

A picture of food could also be on the card if it is simple, but not sure how it would look with Fenwick. I am open to ideas for both Fenwick and a picture of a food item.

Other font style are fine as long as they are easy to read.

```html
<!DOCTYPE html>
<html lang="en">
<head>
<meta charset="utf-8">
<title>Fenwick Nutrition Therapy – Business Card</title>
<link href="https://fonts.googleapis.com/css2?family=Gelasio&family=Tinos&display=swap" rel="stylesheet">
<style>
  :root {
    --stage: #12302a;
    --card-green: #a6ff00;
    --ink-light: #ffffff;
    --ink-faint: rgba(255, 255, 255, 0.55);
    --moon-core: rgba(240, 255, 200, 0.55);
    --moon-edge: rgba(225, 255, 170, 0.25);
    --shadow-soft: rgba(60, 90, 0, 0.55);
  }
  * { box-sizing: border-box; margin: 0; padding: 0; }
  html, body { width: 1200px; height: 1000px; overflow: hidden; }
  body { background: var(--stage); position: relative; font-family: "Tinos", serif; }

  .card {
    position: absolute;
    width: 790px;
    height: 451px;
    background: var(--card-green);
    overflow: hidden;
    box-shadow: 0 8px 24px rgba(0, 0, 0, 0.45);
    color: var(--ink-light);
    text-shadow: 1px 2px 2px var(--shadow-soft);
  }
  .card--front { left: 20px; top: 22px; }
  .card--back { left: 372px; top: 515px; width: 791px; }

  .moon-art {
    position: absolute;
    width: 400px;
    height: 400px;
    border-radius: 50%;
    background: radial-gradient(circle at 45% 45%, var(--moon-core), var(--moon-edge) 75%, rgba(225,255,170,0.15));
  }
  .card--front .moon-art { left: -145px; top: 25px; }
  .card--back .moon-art { left: 528px; top: 35px; }

  .brand-name {
    font-family: "Gelasio", serif;
    font-weight: 400;
    white-space: nowrap;
  }
  .card--front .brand-name {
    position: absolute;
    right: 18px;
    top: 12px;
    font-size: 54px;
  }
  .practitioner {
    position: absolute;
    right: 18px;
    top: 140px;
    text-align: right;
    font-family: "Gelasio", serif;
    line-height: 1;
  }
  .practitioner__name { font-size: 42px; }
  .practitioner__credentials { font-size: 31px; margin-top: 4px; }

  .contact-list {
    position: absolute;
    right: 24px;
    top: 283px;
    list-style: none;
    text-align: right;
    font-size: 27px;
    line-height: 37.5px;
  }
  .contact-list .label { text-decoration: underline; text-underline-offset: 4px; }

  .card--back .brand-name {
    position: absolute;
    left: 22px;
    top: 12px;
    font-size: 56px;
    color: var(--ink-faint);
  }
  .appointment-heading {
    position: absolute;
    left: 25px;
    top: 68px;
    font-family: "Gelasio", serif;
    font-size: 40px;
  }
  .appointment-columns {
    position: absolute;
    left: 262px;
    top: 118px;
    font-family: "Gelasio", serif;
    font-size: 40px;
    word-spacing: 6px;
  }
  .appointment-columns .divider { margin: 0 18px; }

  .appointment-lines {
    position: absolute;
    left: 38px;
    top: 195px;
    width: 735px;
    display: grid;
    grid-template-columns: 332px 332px;
    column-gap: 71px;
    row-gap: 57px;
  }
  .write-line {
    height: 8px;
    border-bottom: 4px dotted var(--ink-light);
  }
</style>
</head>
<body>

  <section class="card card--front" aria-label="Business card front">
    <div class="moon-art" role="img" aria-label="Photograph of a pale full moon"></div>
    <h1 class="brand-name">Fenwick Nutrition Therapy</h1>
    <div class="practitioner">
      <p class="practitioner__name">Dara Ellis Fenwick</p>
      <p class="practitioner__credentials">MS, RD, LDN</p>
    </div>
    <ul class="contact-list">
      <li><span class="label">Fax</span>: 865.555.0171</li>
      <li><span class="label">Phone</span>: 865.555.0148</li>
      <li><span class="label">Email</span>: dfenwick@example.net</li>
      <li><span class="label">Address</span>: 4410 Willow Bend Road, Knoxville, TN 37922</li>
    </ul>
  </section>

  <section class="card card--back" aria-label="Business card back">
    <div class="moon-art" role="img" aria-label="Photograph of a pale full moon"></div>
    <h2 class="brand-name">Fenwick Nutrition Therapy</h2>
    <p class="appointment-heading">Your next appointment:</p>
    <p class="appointment-columns">Date<span class="divider">|</span>Time</p>
    <div class="appointment-lines">
      <div class="write-line"></div><div class="write-line"></div>
      <div class="write-line"></div><div class="write-line"></div>
      <div class="write-line"></div><div class="write-line"></div>
      <div class="write-line"></div><div class="write-line"></div>
    </div>
  </section>

</body>
</html>
```